Brightmere Ledgers New Website

Please review the attached Design Brief with additional details. Thank you!

The goal is to create a website that effectively communicates the benefits of BrightMere Ledgers to eye care professionals. The website should streamline the process of understanding and utilizing WellPath Ledgers' services, emphasizing improved patient outcomes, increased referrals, and enhanced patient engagement.

Target Market(s)

Eyecare Professionals

Number of Pages Required

4 page

```html
<!DOCTYPE html>
<html lang="en">
<head>
<meta charset="utf-8">
<title>Brightmere Ledgers</title>
<link href="https://fonts.googleapis.com/css2?family=Arimo:wght@400;500;700&family=Open+Sans:wght@400;600&family=Crimson+Text:wght@400&display=swap" rel="stylesheet">
<style>
:root{
  --blue:#0d6efd;
  --blue-deep:#1a47b8;
  --orange:#f6a623;
  --ink:#1d1d1f;
  --text:#444;
  --light:#f4f5f7;
  --line:#e3e3e3;
  --black:#0a0a0a;
  --white:#fff;
}
*{margin:0;padding:0;box-sizing:border-box}
html,body{width:1200px;height:4435px;overflow:hidden}
body{position:relative;font-family:"Arimo",Arial,sans-serif;color:var(--ink);background:var(--white)}
.abs{position:absolute}
section,header,footer{position:absolute;left:0;width:1200px}
.mark{display:inline-block;width:14px;height:14px;background:var(--orange)}
.sec-mark{position:absolute;width:18px;height:18px;background:var(--orange);left:50%;margin-left:-9px}
.sec-title{position:absolute;left:0;width:1200px;text-align:center;font-size:34px;font-weight:700;color:var(--ink)}
.btn{position:absolute;display:flex;align-items:center;justify-content:center;background:var(--blue);color:#fff;font-weight:700;font-size:15px;border-radius:5px;text-decoration:none}
.ph{position:absolute}

.site-header{top:0;height:129px;background:#fff;border-top:4px solid var(--orange)}
.brand{position:absolute;left:110px;top:36px;display:flex;align-items:center;gap:10px}
.brand-name{font-size:32px;font-weight:500;color:var(--blue-deep);line-height:1}
.call{position:absolute;left:907px;top:16px;display:flex;gap:14px;align-items:center}
.call small{display:block;font-size:14px;color:#333}
.call b{font-size:17px;color:#111}
.nav{position:absolute;top:82px;font-size:15px;color:#333}

.hero{top:129px;height:557px}
.hero-bg{width:1200px;height:557px;background:linear-gradient(90deg,#1d4fc4 0%,#2f6ad6 30%,#c9d2de 55%,#e8e6e2 100%)}
.hero h2{position:absolute;left:110px;font-weight:400;color:#fff}
.dots span{position:absolute;left:47px;width:12px;height:12px;border:2px solid var(--orange);border-radius:50%}

.about{top:686px;height:549px}
.about h2{position:absolute;left:622px;top:124px;font-size:34px;font-weight:700}
.about p{position:absolute;left:622px;top:196px;width:466px;font-family:"Open Sans",sans-serif;font-size:13px;line-height:24.7px;color:var(--text)}

.services{top:1235px;height:565px;background:var(--light)}
.card{position:absolute;top:187px;width:222px;height:295px;background:#fff;border-radius:6px;box-shadow:0 2px 8px rgba(0,0,0,.08);overflow:hidden}
.card .ph{left:0;top:0;width:222px;height:196px}
.card h3{position:absolute;left:18px;top:212px;width:190px;font-size:16px;font-weight:500;line-height:26px}
.card .more{position:absolute;left:18px;top:265px;font-size:11px;font-weight:700;color:var(--orange)}

.benefits{top:1800px;height:499px}
.benefit{position:absolute;top:211px;width:230px;text-align:center}
.benefit svg{display:block;margin:0 auto}
.benefit h3{margin-top:22px;font-size:21px;font-weight:700}
.benefit p{margin:22px auto 0;width:200px;font-size:12.5px;line-height:23px;color:var(--text)}

.pricing{top:2299px;height:556px;background:var(--blue-deep)}
.pricing .lead{position:absolute;left:110px;color:#fff}
.plan{position:absolute;top:81px;width:352px;height:394px;background:#fff;border-radius:10px;text-align:center}
.plan h3{margin-top:50px;font-size:20px;font-weight:700}
.plan .desc{margin:22px auto 0;width:290px;font-size:14px;line-height:25px;color:var(--text)}
.pill{margin:28px auto 0;height:50px;border-radius:25px;box-shadow:0 2px 10px rgba(0,0,0,.12);display:flex;align-items:center;justify-content:center;gap:12px;color:var(--orange);font-size:20px;font-weight:700}
.pill span{font-size:16px;font-weight:400;border-left:1px solid var(--line);padding-left:12px}
.ticks{margin:24px 0 0 60px;text-align:left;font-size:15px;color:var(--text)}
.ticks li{list-style:none;display:flex;gap:14px;align-items:center;height:32px}

.testimonials{top:2855px;height:644px}
.quote-mark{position:absolute;font-family:"Crimson Text",serif;font-size:240px;line-height:1;color:#ececec}

.contact{top:3499px;height:575px;background:#f6f7f9}
.field{position:absolute;background:#fff;box-shadow:0 2px 10px rgba(0,0,0,.06);font-size:17px;color:#555;padding:0 26px;display:flex;align-items:center;justify-content:space-between}

.site-footer{top:4074px;height:361px;background:var(--black);color:#fff}
.site-footer h4{position:absolute;top:66px;font-size:20px;font-weight:700}
.links{position:absolute;top:110px;list-style:none;font-size:14.5px}
.links li{height:25.8px;display:flex;gap:14px}
.links li::before{content:"»";color:var(--blue)}
.social{position:absolute;top:198px;width:38px;height:38px;border-radius:50%;background:var(--orange);border:2px solid #fff}
.fc{position:absolute;left:847px;font-size:14.5px;display:flex;gap:10px;line-height:25px}
</style>
</head>
<body>

<header class="site-header">
  <div class="brand"><span class="mark" style="width:24px;height:24px"></span><span class="brand-name">Brightmere Ledgers</span></div>
  <a class="btn" style="left:752px;top:13px;width:123px;height:45px">Get Started</a>
  <div class="call">
    <svg width="34" height="34" viewBox="0 0 24 24"><path fill="#1a47b8" d="M6.6 10.8a15 15 0 0 0 6.6 6.6l2.2-2.2c.3-.3.7-.4 1-.2 1.1.4 2.3.6 3.6.6.6 0 1 .4 1 1V20c0 .6-.4 1-1 1A17 17 0 0 1 3 4c0-.6.4-1 1-1h3.5c.6 0 1 .4 1 1 0 1.3.2 2.5.6 3.6.1.3 0 .7-.2 1z"/></svg>
    <div><small>Call Us</small><b>(844-555-0148)</b></div>
  </div>
  <span class="nav" style="left:410px">Home</span>
  <span class="nav" style="left:486px">About Us</span>
  <span class="nav" style="left:584px">Services</span>
  <span class="nav" style="left:673px">Pricing</span>
  <span class="nav" style="left:754px">Testimonials</span>
  <span class="nav" style="left:878px">Blog</span>
  <span class="nav" style="left:940px">Contact Us</span>
  <span class="nav" style="left:1050px">FAQs</span>
</header>

<section class="hero">
  <div class="hero-bg" role="img" aria-label="Photo of a smiling patient talking with a clinician holding a clipboard"></div>
  <h2 style="top:118px;font-size:38px">Welcome To</h2>
  <h2 style="top:178px;font-size:68px;font-weight:700;color:var(--orange)">Brightmere</h2>
  <h2 style="top:271px;font-size:68px;font-weight:700">Ledgers</h2>
  <a class="btn" style="left:110px;top:384px;width:124px;height:47px">Get Started</a>
  <div class="dots"><span style="top:388px"></span><span style="top:403px;background:var(--orange)"></span><span style="top:418px"></span></div>
</section>

<section class="about">
  <div class="ph" role="img" aria-label="Photo of a doctor writing on a clipboard" style="left:110px;top:85px;width:334px;height:292px;background:linear-gradient(135deg,#e9eef3,#b9c6d3);border-radius:6px"></div>
  <div class="ph" role="img" aria-label="Photo of a doctor with an elderly patient" style="left:343px;top:289px;width:205px;height:175px;background:linear-gradient(135deg,#8fb1cc,#d8dde2);border:4px solid #fff"></div>
  <span class="mark" style="position:absolute;left:622px;top:92px;width:18px;height:18px"></span>
  <h2>About The Registry</h2>
  <p>Brightmere Ledgers can guide your clinical decision making by providing you with "real-time" clinical outcome analytics. The analytics are designed to look at practical issues affecting the quality of care you deliver to your patients. These issues impact the efficiency and viability of your practice. There are various types of registries which can be used in different ways. Some registries are known as "Reporting Registries" which are designed to report merit-based incentive payment systems (MIPS) scores.</p>
  <a class="btn" style="left:622px;top:401px;width:124px;height:46px">Learn More</a>
</section>

<section class="services">
  <span class="sec-mark" style="top:74px"></span>
  <h2 class="sec-title" style="top:100px">Our Services</h2>
  <div class="card" style="left:110px"><div class="ph" role="img" aria-label="Photo of a clinician reviewing notes with a patient" style="background:linear-gradient(135deg,#d9dcd8,#8a9aa8)"></div><h3>Diabetes Management Registry</h3><span class="more">Learn More ›</span></div>
  <div class="card" style="left:362px"><div class="ph" role="img" aria-label="Photo of a surgical instrument holding a lens" style="background:linear-gradient(135deg,#5b8fe0,#2f62c9)"></div><h3>Cataract Extraction Registry</h3><span class="more">Learn More ›</span></div>
  <div class="card" style="left:615px"><div class="ph" role="img" aria-label="Photo of a person applying eye drops" style="background:linear-gradient(135deg,#c9b2a0,#7b5a48)"></div><h3 style="top:225px">Dry Eye Registry</h3><span class="more">Learn More ›</span></div>
  <div class="card" style="left:866px"><div class="ph" role="img" aria-label="Photo of a child at an eye chart wearing trial glasses" style="background:linear-gradient(135deg,#eef0f2,#a9c3de)"></div><h3 style="top:225px">Myopia Registry</h3><span class="more">Learn More ›</span></div>
</section>

<section class="benefits">
  <span class="sec-mark" style="top:94px"></span>
  <h2 class="sec-title" style="top:122px">Our Benefits</h2>
  <div class="benefit" style="left:95px"><svg width="72" height="72" viewBox="0 0 72 72" fill="none" stroke="#1a5fd1" stroke-width="3"><path d="M36 52 18 34a10 10 0 0 1 18-12 10 10 0 0 1 18 12z"/><path d="M36 28v14M29 35h14"/></svg><h3>Lorem ipsum do</h3><p>Lorem ipsum dolor sit ameat, consectetur adipiscing elit, sed do eiusmodeiusmod</p></div>
  <div class="benefit" style="left:355px"><svg width="72" height="72" viewBox="0 0 72 72" fill="none" stroke="#1a5fd1" stroke-width="3"><rect x="16" y="6" width="36" height="58" rx="3"/><path d="M34 14v14M27 21h14M24 40h20M24 48h14"/></svg><h3>Lorem ipsum do</h3><p>Lorem ipsum dolor sit ameat, consectetur adipiscing elit, sed do eiusmodeiusmod</p></div>
  <div class="benefit" style="left:615px"><svg width="72" height="72" viewBox="0 0 72 72" fill="none" stroke="#1a5fd1" stroke-width="3"><rect x="12" y="22" width="48" height="42" rx="4"/><rect x="26" y="6" width="20" height="16"/><path d="M36 32v22M25 43h22"/></svg><h3>Lorem ipsum do</h3><p>Lorem ipsum dolor sit ameat, consectetur adipiscing elit, sed do eiusmodeiusmod</p></div>
  <div class="benefit" style="left:875px"><svg width="72" height="72" viewBox="0 0 72 72" fill="none" stroke="#1a5fd1" stroke-width="3"><circle cx="30" cy="20" r="12"/><path d="M8 64c0-14 10-24 22-24"/><circle cx="50" cy="50" r="12"/><path d="M50 43v14M43 50h14"/></svg><h3>Lorem ipsum do</h3><p>Lorem ipsum dolor sit ameat, consectetur adipiscing elit, sed do eiusmodeiusmod</p></div>
</section>

<section class="pricing">
  <span class="mark" style="position:absolute;left:113px;top:142px;width:20px;height:20px"></span>
  <h2 class="lead" style="top:180px;font-size:34px;font-weight:700;line-height:52px">Our<br>Prices</h2>
  <p class="lead" style="top:294px;font-size:14px;line-height:26px">Lorem ipsum dolor sit amet,<br>consectetur adipiscing</p>
  <a class="btn" style="left:110px;top:373px;width:124px;height:47px">Learn More</a>
  <div class="plan" style="left:365px">
    <h3>Initial One-Time Setup</h3>
    <p class="desc">Lorem ipsum dolor sit amet, consectetur adipiscing elit, sed do eiusmod tempor</p>
    <div class="pill" style="width:165px">$1000</div>
    <ul class="ticks"><li><svg width="18" height="14" viewBox="0 0 18 14"><path d="M1 7l5 5L17 1" fill="none" stroke="#f6a623" stroke-width="2"/></svg>Lorem ipsum dolor sit amet,</li><li><svg width="18" height="14" viewBox="0 0 18 14"><path d="M1 7l5 5L17 1" fill="none" stroke="#f6a623" stroke-width="2"/></svg>Lorem ipsum dolor sit amet,</li></ul>
    <a class="btn" style="left:114px;top:322px;width:123px;height:48px">View Plan</a>
  </div>
  <div class="plan" style="left:735px">
    <h3>Monthly Subscription</h3>
    <p class="desc">Lorem ipsum dolor sit amet, consectetur adipiscing elit, sed do eiusmod tempor</p>
    <div class="pill" style="width:200px">$99<span>Per Location</span></div>
    <ul class="ticks"><li><svg width="18" height="14" viewBox="0 0 18 14"><path d="M1 7l5 5L17 1" fill="none" stroke="#f6a623" stroke-width="2"/></svg>Lorem ipsum dolor sit amet,</li><li><svg width="18" height="14" viewBox="0 0 18 14"><path d="M1 7l5 5L17 1" fill="none" stroke="#f6a623" stroke-width="2"/></svg>Lorem ipsum dolor sit amet,</li></ul>
    <a class="btn" style="left:114px;top:322px;width:123px;height:48px">View Plan</a>
  </div>
</section>

<section class="testimonials">
  <span class="sec-mark" style="top:92px"></span>
  <h2 class="sec-title" style="top:122px">Our Testimonials</h2>
  <div class="ph" role="img" aria-label="Portrait photo of the reviewing doctor" style="left:546px;top:203px;width:110px;height:110px;border-radius:50%;background:linear-gradient(135deg,#5a6472,#1f2630);border:3px solid var(--orange)"></div>
  <span class="quote-mark" style="left:104px;top:270px">“</span>
  <span class="quote-mark" style="left:958px;top:452px">”</span>
  <h3 style="position:absolute;top:333px;width:1200px;text-align:center;font-size:25px;font-weight:400;color:#333">Dr. Daniel Hart</h3>
  <p style="position:absolute;left:185px;top:385px;width:830px;text-align:center;font-family:'Crimson Text',serif;font-size:18px;line-height:30px;color:#333">Working with BrightMere Ledgers is the best investment that I have ever made in my practices. Access to my clinical outcome data help build pcp referrals. Actually, in one day, I received 40 new diabetic referrals.</p>
  <span class="abs" style="left:548px;top:529px;width:24px;height:4px;background:#ccc;border-radius:2px"></span>
  <span class="abs" style="left:588px;top:529px;width:24px;height:4px;background:var(--blue-deep);border-radius:2px"></span>
  <span class="abs" style="left:628px;top:529px;width:24px;height:4px;background:#ccc;border-radius:2px"></span>
</section>

<section class="contact">
  <span class="sec-mark" style="top:76px"></span>
  <h2 class="sec-title" style="top:104px">Contact Us</h2>
  <div class="field" style="left:148px;top:184px;width:425px;height:74px">Your Name<svg width="18" height="18" viewBox="0 0 18 18" fill="none" stroke="#555" stroke-width="1.5"><circle cx="9" cy="9" r="8"/><circle cx="9" cy="7" r="3"/></svg></div>
  <div class="field" style="left:148px;top:298px;width:425px;height:76px">Email Address<svg width="18" height="14" viewBox="0 0 18 14" fill="none" stroke="#555" stroke-width="1.5"><rect x="1" y="1" width="16" height="12"/><path d="M1 1l8 6 8-6"/></svg></div>
  <div class="field" style="left:148px;top:413px;width:425px;height:74px">Phone<svg width="16" height="16" viewBox="0 0 24 24"><path fill="#555" d="M6.6 10.8a15 15 0 0 0 6.6 6.6l2.2-2.2c.3-.3.7-.4 1-.2 1.1.4 2.3.6 3.6.6.6 0 1 .4 1 1V20c0 .6-.4 1-1 1A17 17 0 0 1 3 4c0-.6.4-1 1-1h3.5c.6 0 1 .4 1 1 0 1.3.2 2.5.6 3.6.1.3 0 .7-.2 1z"/></svg></div>
  <div class="field" style="left:611px;top:184px;width:441px;height:224px;align-items:flex-start;padding-top:24px">How can we help?<svg width="18" height="16" viewBox="0 0 18 16" fill="none" stroke="#555" stroke-width="1.5"><path d="M2 2h14v9H8l-4 3v-3H2z"/></svg></div>
  <a class="btn" style="left:611px;top:427px;width:157px;height:62px;font-size:17px;border-radius:3px">SUBMIT NOW</a>
</section>

<footer class="site-footer">
  <div style="position:absolute;left:112px;top:90px;display:flex;align-items:center;gap:8px"><span class="mark" style="background:#fff;width:22px;height:22px"></span><span style="font-size:29px;font-weight:500">Brightmere Ledgers</span></div>
  <span class="social" style="left:110px"></span><span class="social" style="left:153px"></span><span class="social" style="left:196px"></span><span class="social" style="left:239px"></span>
  <span class="abs" style="left:389px;top:56px;width:1px;height:210px;background:#333"></span>
  <h4 style="left:432px">Quick Links</h4>
  <ul class="links" style="left:432px"><li>Home</li><li>About Us</li><li>Services</li><li>Pricing</li><li>Testimonials</li><li>More</li></ul>
  <h4 style="left:622px">Our Company</h4>
  <ul class="links" style="left:622px"><li>Terms &amp; Conditions</li><li>Privacy Policy</li><li>About Us</li><li>Support</li></ul>
  <h4 style="left:847px">Contact Us</h4>
  <div class="fc" style="top:106px"><svg width="14" height="20" viewBox="0 0 14 20"><path fill="#fff" d="M7 0a7 7 0 0 1 7 7c0 5-7 13-7 13S0 12 0 7a7 7 0 0 1 7-7zm0 4a3 3 0 1 0 0 6 3 3 0 0 0 0-6z"/></svg><span>Lorem ipsum dolor sit<br>amet, consectetur adipiscing</span></div>
  <div class="fc" style="top:174px"><svg width="16" height="16" viewBox="0 0 24 24"><path fill="#fff" d="M6.6 10.8a15 15 0 0 0 6.6 6.6l2.2-2.2c.3-.3.7-.4 1-.2 1.1.4 2.3.6 3.6.6.6 0 1 .4 1 1V20c0 .6-.4 1-1 1A17 17 0 0 1 3 4c0-.6.4-1 1-1h3.5c.6 0 1 .4 1 1 0 1.3.2 2.5.6 3.6.1.3 0 .7-.2 1z"/></svg>844-555-0148</div>
  <div class="fc" style="top:216px"><svg width="16" height="14" viewBox="0 0 16 12"><path fill="#fff" d="M0 0h16v12H0zM1 1l7 5 7-5"/></svg>ContactUs@BrightMereLedgers.com</div>
  <span class="abs" style="left:110px;top:283px;width:980px;height:1px;background:#333"></span>
  <p style="position:absolute;top:305px;width:1200px;text-align:center;font-size:14px">©Copyrights 2023 Brightmere Ledgers &nbsp;|&nbsp;&nbsp; All Rights Reserved</p>
</footer>

</body>
</html>
```